Website design for SaaS -solution

We are B2B SaaS company. (Korbel.io) Our software brings leads by enriching company profiles with external data. We want to take load off from marketing and sales directors by bringing them sales leads.

Our core values that we want to communicate:
-Data driven
-Easy going and easy to use
-Sincere and honest
-Humble
-lively

We would like to see designs that obey our colours (logos attached) but also the website should be lively and visual / photo intensive. We only use few sentences to power our message. Here are few examples:

http://www.example-plinsor.com/
https://www.example-tavvo.com/

We will also make a video that we post in the front cover. Our current website is www.korbel.io. The font we would like to use is Avenir Next or similar

• Avenir Next

0455a3
ec1f27
9bcb3c
85acd3

• 1 page: the main page (attached is brief) (This is most important one)
• 2. page: , a design where we can post content such as slides, e-papers etc (e.g.. http://www.example-quendrapoint.com/eu/industries/)
• 3. page: a basic template that can be used for various needs ( team-page, jobs, page, etc)

```html
<!DOCTYPE html>
<html lang="en">
<head>
<meta charset="utf-8">
<title>Kelvaro – Home</title>
<link href="https://fonts.googleapis.com/css2?family=Raleway:wght@400;500;600;700&family=Open+Sans:wght@400;600&display=swap" rel="stylesheet">
<style>
:root{
  --brand-blue:#0a4aa3;
  --bar-blue:#2b5ba8;
  --accent-green:#8cc63f;
  --accent-red:#e2132a;
  --light-blue:#85acd3;
  --text-grey:#666;
  --dark:#1c1c1c;
  --darker:#141414;
  --white:#fff;
}
*{margin:0;padding:0;box-sizing:border-box}
html,body{width:717px;height:1200px;overflow:hidden}
body{position:relative;background:var(--white);font-family:"Open Sans",Arial,sans-serif;color:#333}
h1,h2,h3,h4{font-weight:400}
.abs{position:absolute}
.topbar{left:0;top:0;width:717px;height:30px;background:var(--bar-blue)}
.social-top{left:59px;top:6px;display:flex;gap:5px}
.social-top span{width:18px;height:18px;border-radius:3px;background:rgba(255,255,255,.28);display:block}
.top-links{right:76px;top:0;height:30px;display:flex;gap:24px;align-items:center;color:var(--white);font-size:7.2px;text-transform:uppercase}
.top-links span{display:flex;align-items:center;gap:4px}
.header{left:0;top:30px;width:717px;height:64px;background:var(--white)}
.logo{left:59px;top:46px;display:flex;align-items:center;gap:8px;font-family:"Raleway",sans-serif;font-size:30px;color:#8a8a8a;letter-spacing:.5px}
.logo i{width:22px;height:22px;border-radius:50%;background:var(--brand-blue);display:block}
.nav{right:80px;top:58px;display:flex;gap:30px;font-family:"Raleway",sans-serif;font-size:8.5px;color:#444;text-transform:uppercase}
.nav .active{color:var(--brand-blue)}
.hero{left:0;top:94px;width:717px;height:259px;background:linear-gradient(180deg,#6e8fb7 0%,#4c6684 55%,#445a43 100%)}
.hero-panel{left:471px;top:94px;width:187px;height:259px;background:rgba(34,84,170,.72)}
.hero-title{left:482px;top:124px;font-family:"Raleway",sans-serif;font-size:16px;font-weight:400;color:var(--white)}
.hero-text{left:485px;top:152px;width:168px;font-family:Arial,sans-serif;font-size:7.6px;line-height:13px;color:var(--white)}
.btn-info{left:486px;top:228px;width:64px;height:22px;background:var(--accent-green);color:var(--white);font-size:7px;font-weight:600;display:flex;align-items:center;justify-content:center;text-transform:uppercase}
.badge{left:490px;top:292px;width:142px;height:34px;border-radius:4px;background:rgba(255,255,255,.22)}
.arrow{top:212px;width:30px;height:30px;border-radius:50%;border:2px solid rgba(255,255,255,.35)}
.email{left:59px;top:289px;width:275px;height:31px;background:var(--white);font-size:7.5px;color:#333;padding-left:12px;display:flex;align-items:center}
.submit{left:334px;top:289px;width:73px;height:31px;background:var(--brand-blue);color:var(--white);font-size:9.5px;font-weight:600;display:flex;align-items:center;justify-content:center}
.section-title{left:0;width:717px;text-align:center;font-family:"Raleway",sans-serif;color:var(--brand-blue)}
.section-sub{left:108px;width:500px;text-align:center;font-family:Arial,sans-serif;font-size:6.8px;line-height:13px;color:var(--text-grey)}
.feature{width:170px;text-align:center}
.feature .ring{width:64px;height:64px;margin:0 auto;border-radius:50%;padding:2px}
.feature .ring div{width:100%;height:100%;border-radius:50%;border:2px solid var(--white);display:flex;align-items:center;justify-content:center}
.feature h3{margin-top:12px;font-family:"Raleway",sans-serif;font-weight:500;font-size:10px;color:#333;text-transform:uppercase}
.feature p{margin-top:6px;font-family:Arial,sans-serif;font-size:6.4px;line-height:11.5px;color:#555}
.testimonials{left:0;top:608px;width:717px;height:230px;background:linear-gradient(90deg,#5d6a78 0%,#3d4957 45%,#1f2731 100%)}
.testi-title{left:0;top:662px;width:717px;text-align:center;font-family:"Raleway",sans-serif;font-weight:700;font-size:13px;color:var(--white)}
.testi-text{left:120px;top:695px;width:477px;text-align:center;font-family:Arial,sans-serif;font-size:7.2px;line-height:12px;color:var(--white)}
.quote{font-family:Georgia,serif;font-size:20px;color:rgba(255,255,255,.7)}
.avatar{left:282px;top:746px;width:52px;height:52px;border-radius:50%;border:3px solid var(--white);background:linear-gradient(160deg,#9fb7cf,#2e3e58)}
.person{left:341px;top:759px;font-family:"Raleway",sans-serif;font-size:8px;color:var(--white);line-height:12px}
.person b{font-weight:400;color:var(--accent-green)}
.person i{font-style:italic}
.client{top:924px;width:108px;height:62px;border:4px solid #eee;display:flex;align-items:center;justify-content:center;font-family:"Open Sans",sans-serif;font-size:14px;font-weight:600;color:#9a9a9a}
.chev{top:936px}
.footer{left:0;top:1016px;width:717px;height:144px;background:var(--dark)}
.footer-bottom{left:0;top:1160px;width:717px;height:40px;background:var(--darker);border-top:1px solid #2a2a2a}
.f-head{top:1039px;font-family:"Raleway",sans-serif;font-size:8px;font-weight:500;color:#4f8fd8;text-transform:uppercase}
.f-list{font-size:6.8px;color:#cfcfcf;line-height:14.4px}
.contact-row{display:flex;gap:8px;align-items:flex-start;margin-bottom:4px}
.contact-row svg{flex:none;margin-top:3px}
.tweet{font-size:6.8px;color:#cfcfcf;line-height:10px;width:140px}
.tweet em{display:block;color:#4f8fd8;font-size:5.6px;margin-bottom:8px}
.follow-circles{left:529px;top:1106px;display:flex;gap:6px}
.follow-circles span{width:23px;height:23px;border-radius:50%;border:1.5px solid var(--white);display:block}
.copyright{left:0;top:1176px;width:717px;text-align:center;font-size:6.5px;color:#ddd}
</style>
</head>
<body>

<div class="abs topbar"></div>
<div class="abs social-top" aria-label="Social links">
  <span></span><span></span><span></span><span></span><span></span><span></span>
</div>
<div class="abs top-links">
  <span>Login</span><span>Blog</span><span>Contact +1.800.555.014</span><span>Americas (English)</span>
</div>

<div class="abs header"></div>
<div class="abs logo"><i></i>kelvaro</div>
<nav class="abs nav">
  <span class="active">Home</span><span>Team</span><span>Products</span><span>Customer</span><span>Careers</span>
</nav>

<div class="abs hero" role="img" aria-label="Photo of city skyscrapers under a blue sky"></div>
<div class="abs hero-panel"></div>
<div class="abs arrow" style="left:22px"></div>
<div class="abs arrow" style="left:666px"></div>
<h1 class="abs hero-title">WHAT KELVARO IS</h1>
<p class="abs hero-text">Whether it's a corporate acquisition, investment, new office or even a change in the target comthe information reaches the sales team.We go lore through &nbsp;behavior signals. We gather &nbsp;that sales potential perspective</p>
<div class="abs btn-info">More Info</div>
<div class="abs badge" role="img" aria-label="Event badge"></div>
<div class="abs email">Enter your email</div>
<div class="abs submit">SUBMIT</div>

<h2 class="abs section-title" style="top:377px;font-size:19px">Is B2B Sales Completely Gone Digital?</h2>
<p class="abs section-sub" style="top:411px">We go through open data and identify with prospective purchase behavior signals. We gather every day a huge amount of information that organizations focus our right and we value their sales potential perspective.</p>

<div class="abs feature" style="left:71px;top:462px">
  <div class="ring" style="border:1.5px solid var(--brand-blue)"><div style="background:var(--brand-blue)">
    <svg width="26" height="22" viewBox="0 0 26 22"><path d="M1 1v20h24" stroke="#fff" stroke-width="2" fill="none"/><rect x="6" y="11" width="3" height="8" fill="#fff"/><rect x="11" y="6" width="3" height="13" fill="#fff"/><rect x="16" y="9" width="3" height="10" fill="#fff"/><rect x="21" y="4" width="3" height="15" fill="#fff"/></svg>
  </div></div>
  <h3>Marketing</h3>
  <p>It is a long established fact that a reader will be distracted by the readable content of a page when looking at its letters, as opposed to able Englis</p>
</div>
<div class="abs feature" style="left:273px;top:462px">
  <div class="ring" style="border:1.5px solid var(--accent-green)"><div style="background:var(--accent-green)">
    <svg width="26" height="26" viewBox="0 0 26 26"><path d="M3 3h10l11 11-10 10L3 13z" fill="#fff"/><circle cx="8" cy="8" r="2" fill="#8cc63f"/></svg>
  </div></div>
  <h3>Sales</h3>
  <p>It is a long established fact that a reader will be distracted by the readable content of a page when looking at its letters, as opposed to able Englis</p>
</div>
<div class="abs feature" style="left:477px;top:462px">
  <div class="ring" style="border:1.5px solid var(--accent-red)"><div style="background:var(--accent-red)">
    <svg width="28" height="22" viewBox="0 0 28 22"><circle cx="14" cy="6" r="4" fill="#fff"/><path d="M7 20c0-5 3-8 7-8s7 3 7 8z" fill="#fff"/><circle cx="5" cy="8" r="3" fill="#fff"/><path d="M0 20c0-4 2-7 5-7s4 2 4 3v4z" fill="#fff"/><circle cx="23" cy="8" r="3" fill="#fff"/><path d="M28 20c0-4-2-7-5-7s-4 2-4 3v4z" fill="#fff"/></svg>
  </div></div>
  <h3>Industry Expert</h3>
  <p>It is a long established fact that a reader will be distracted by the readable content of a page when looking at its letters, as opposed to able Englis</p>
</div>

<div class="abs testimonials" role="img" aria-label="Dark photo of a hand using a touchscreen"></div>
<h2 class="abs testi-title">OUR TESTIMONIALS</h2>
<span class="abs quote" style="left:116px;top:674px">&ldquo;</span>
<p class="abs testi-text">When you engage us, you have access to an entire team of American university professionals with relevant firsthand admissions experience, education, and knowledge. Orvane will help you with the key stages of preparation, research, and application to US universities and guide you in your critical first steps into the &nbsp;supervising student visa application procedures, and exploring Financial Aid options.</p>
<span class="abs quote" style="left:540px;top:728px">&rdquo;</span>
<div class="abs avatar" role="img" aria-label="Portrait photo of the reviewer"></div>
<p class="abs person">Name : <b>Aarne Lindqvist - myyntijohtaja, Velora</b><br><i>posed on 25 March 2015</i></p>

<h2 class="abs section-title" style="top:857px;font-size:19px">Our Clients</h2>
<p class="abs section-sub" style="top:890px;left:108px;font-size:8.4px">We go through open data and identify with prospective purchase behavior signals. We gather every day</p>
<svg class="abs chev" style="left:28px" width="10" height="38" viewBox="0 0 10 38"><path d="M9 1L1 19l8 18" stroke="#ccc" fill="none"/></svg>
<div class="abs client" style="left:59px">Mirelle</div>
<div class="abs client" style="left:182px">Otrin</div>
<div class="abs client" style="left:305px">Noventa</div>
<div class="abs client" style="left:428px;font-size:12px">Farwell Grid</div>
<div class="abs client" style="left:549px">Pelora</div>
<svg class="abs chev" style="left:679px" width="10" height="38" viewBox="0 0 10 38"><path d="M1 1l8 18-8 18" stroke="#ccc" fill="none"/></svg>

<footer>
<div class="abs footer"></div>
<h4 class="abs f-head" style="left:59px">Contact Us</h4>
<div class="abs f-list" style="left:59px;top:1064px;width:140px">
  <div class="contact-row"><svg width="9" height="7"><rect width="9" height="7" rx="2" fill="#4f8fd8"/></svg><span>03 5550 0127 (Phone)</span></div>
  <div class="contact-row"><svg width="9" height="7"><rect width="9" height="7" fill="#4f8fd8"/></svg><span>03 5550 0127 &nbsp;(Fax)</span></div>
  <div class="contact-row"><svg width="9" height="7"><rect width="9" height="7" fill="#4f8fd8"/><path d="M0 0l4.5 4L9 0" stroke="#1c1c1c" fill="none"/></svg><span style="text-decoration:underline">admin@kelvaro-mail.example</span></div>
  <div class="contact-row"><svg width="9" height="9"><path d="M4.5 9L1 4a3.5 3.5 0 117 0z" fill="#4f8fd8"/></svg><span style="line-height:10px">PO Box: 4410, Thailand<br>lorem si3844</span></div>
</div>
<h4 class="abs f-head" style="left:210px">Twitter Feed</h4>
<div class="abs" style="left:210px;top:1065px">
  <p class="tweet">@kelvaroteam, Nimbra site theme full responsive is coming soon..<em>4 days ago</em></p>
  <p class="tweet">@kelvaroteam, Nimbra site theme full responsive is coming soon...<em>4 days ago</em></p>
</div>
<h4 class="abs f-head" style="left:399px">About</h4>
<div class="abs f-list" style="left:397px;top:1055px">
  Investors<br>Careers<br>Terms &amp; Condtions of Service<br>Privacy Policy<br>Service Level Agreement<br>Master Commercial Agreement
</div>
<h4 class="abs f-head" style="left:529px">Follow Us</h4>
<p class="abs tweet" style="left:529px;top:1066px;width:135px">Lorem ipsum dolor sit amet, consectetur adipiscing elit. Nulla in purus nibh. Donec ornare felis neque. Nullam tortor!</p>
<div class="abs follow-circles" aria-label="Social profiles"><span></span><span></span><span></span><span></span></div>
<div class="abs footer-bottom"></div>
<p class="abs copyright">© COPY RIGHT2015 KELVARO. ALL &nbsp;RIGHTS RESERVED</p>
</footer>

</body>
</html>
```